Accounting firm needing business card / letterhead designed
Marcus T. Elbering, CPA
marcus@fernquill.com
www.fernquill.com
482 N Harlow Ave Larkmont, ND 43719
701-555-0172

```html
<!DOCTYPE html>
<html lang="en">
<head>
<meta charset="utf-8">
<title>Fernquill Advisors – Business Card</title>
<link href="https://fonts.googleapis.com/css2?family=Roboto:wght@400;700&family=Roboto+Condensed:wght@700&display=swap" rel="stylesheet">
<style>
  :root {
    --navy: #28255e;
    --green: #7cc242;
    --white: #ffffff;
    --backdrop: #8f7457;
    --card-shadow: rgba(0, 0, 0, 0.35);
  }
  html, body {
    margin: 0;
    padding: 0;
    width: 900px;
    height: 1200px;
    overflow: hidden;
    background: var(--backdrop);
    font-family: "Roboto", Arial, sans-serif;
  }
  .canvas {
    position: relative;
    width: 900px;
    height: 1200px;
  }
  .card {
    position: absolute;
    width: 734px;
    height: 429px;
    border-radius: 24px;
    box-shadow: 0 6px 14px var(--card-shadow);
    overflow: hidden;
  }
  .card--front {
    left: 88px;
    top: 133px;
    background: var(--white);
  }
  .card--back {
    left: 82px;
    top: 630px;
    background: var(--navy);
  }

  /* Front */
  .brand-name {
    position: absolute;
    margin: 0;
    font-family: "Roboto", Arial, sans-serif;
    font-weight: 700;
    text-transform: uppercase;
    line-height: 1.05;
  }
  .card--front .brand-name {
    left: 66px;
    top: 176px;
    width: 280px;
    font-size: 36px;
    letter-spacing: 1px;
    color: var(--navy);
  }
  .divider {
    position: absolute;
    left: 366px;
    top: 159px;
    width: 2px;
    height: 113px;
    background: var(--navy);
  }
  .contact {
    position: absolute;
    left: 401px;
    top: 152px;
  }
  .contact__name {
    margin: 0 0 8px;
    font-family: "Roboto Condensed", "Arial Narrow", sans-serif;
    font-weight: 700;
    font-size: 23px;
    color: var(--navy);
    text-transform: uppercase;
    letter-spacing: 0.3px;
  }
  .contact__list {
    list-style: none;
    margin: 0;
    padding: 0;
  }
  .contact__item {
    display: flex;
    align-items: center;
    height: 29px;
    font-size: 18px;
    color: var(--navy);
  }
  .contact__item svg {
    width: 20px;
    height: 20px;
    margin-right: 12px;
    flex: none;
  }
  .address {
    position: absolute;
    margin: 0;
    left: 0;
    right: 0;
    top: 370px;
    display: flex;
    justify-content: center;
    align-items: center;
    font-size: 18px;
    color: var(--navy);
  }
  .address svg {
    width: 18px;
    height: 24px;
    margin-right: 10px;
  }

  /* Back */
  .card--back .brand-name {
    left: 0;
    right: 0;
    top: 186px;
    text-align: center;
    font-size: 54px;
    letter-spacing: 2px;
    color: var(--white);
  }
  .back-website {
    position: absolute;
    margin: 0;
    left: 0;
    right: 0;
    top: 369px;
    text-align: center;
    font-weight: 700;
    font-size: 21px;
    letter-spacing: 1.2px;
    color: var(--white);
  }
</style>
</head>
<body>
<main class="canvas">

  <section class="card card--front" aria-label="Business card front">
    <h1 class="brand-name">Fernquill Advisors</h1>
    <div class="divider"></div>

    <div class="contact">
      <h2 class="contact__name">Marcus T. Elbering, CPA</h2>
      <ul class="contact__list">
        <li class="contact__item">
          <svg viewBox="0 0 20 20" aria-hidden="true">
            <path d="M2 7 C2 3 18 3 18 7 L15 8.5 L13 6.5 L7 6.5 L5 8.5 Z" fill="var(--green)"/>
            <path d="M6 9 L14 9 L17 16 L3 16 Z" fill="var(--green)"/>
            <circle cx="10" cy="12.5" r="1.8" fill="var(--white)"/>
          </svg>
          701-555-0172
        </li>
        <li class="contact__item">
          <svg viewBox="0 0 20 20" aria-hidden="true">
            <rect x="1.5" y="4" width="17" height="12" fill="var(--green)"/>
            <path d="M1.5 4 L10 11 L18.5 4" fill="none" stroke="var(--white)" stroke-width="1.4"/>
          </svg>
          marcus@fernquill.com
        </li>
        <li class="contact__item">
          <svg viewBox="0 0 20 20" aria-hidden="true">
            <g fill="none" stroke="var(--green)" stroke-width="1.5">
              <circle cx="10" cy="10" r="8.5"/>
              <ellipse cx="10" cy="10" rx="3.8" ry="8.5"/>
              <line x1="1.5" y1="10" x2="18.5" y2="10"/>
              <line x1="3" y1="5.5" x2="17" y2="5.5"/>
              <line x1="3" y1="14.5" x2="17" y2="14.5"/>
            </g>
          </svg>
          www.fernquill.com
        </li>
      </ul>
    </div>

    <p class="address">
      <svg viewBox="0 0 18 24" aria-hidden="true">
        <path d="M9 1 C4.5 1 1 4.5 1 9 C1 15 9 23 9 23 C9 23 17 15 17 9 C17 4.5 13.5 1 9 1 Z" fill="var(--green)"/>
        <circle cx="9" cy="9" r="3.2" fill="var(--white)"/>
      </svg>
      482 N Harlow Ave Larkmont, ND 43719
    </p>
  </section>

  <section class="card card--back" aria-label="Business card back">
    <h2 class="brand-name">Fernquill Advisors</h2>
    <p class="back-website">www.fernquill.com</p>
  </section>

</main>
</body>
</html>
```